Tallow Crest Software PowerPoint template

We are a software company selling endpoint visibility, access and security technology to enterprise-level IT departments.
Our technology helps organizations gain comprehensive visibility into and control over devices accessing their corporate network so they can quickly identify and address suspicious activity on the network that could lead to potential threats like data breaches.
This technology can cost organizations upwards of $1M - depending on the size of the organization. Our primary clients are Meridane 2,000 companies.
We want a professional, polished PowerPoint template that we can use for all company presentations. Please include:
Title page
Section page
General info page
Thank you page
Logo options and color specs are attached.
Please include our tagline on at least the title page: Discover the edge. Optimize the whole.

```html
<!DOCTYPE html>
<html lang="en">
<head>
<meta charset="utf-8">
<title>Tallow Crest Software – Presentation Template</title>
<link rel="stylesheet" href="https://fonts.googleapis.com/css2?family=PT+Sans:ital,wght@0,400;0,700;1,400&family=PT+Sans+Narrow:wght@400;700&display=swap">
<style>
  :root {
    --stage: #1d1d1e;
    --red-hi: #c0262f;
    --red: #a51c24;
    --red-deep: #7e0f16;
    --maroon: #8c1a22;
    --tan: #d99a78;
    --orange-hi: #e0804a;
    --orange: #c25a26;
    --pink-hi: #fdf3f3;
    --pink: #f6e0e0;
    --text: #3a1a1a;
    --white: #ffffff;
  }
  * { box-sizing: border-box; margin: 0; padding: 0; }
  html, body { width: 1200px; height: 900px; overflow: hidden; background: var(--stage); }
  body { position: relative; font-family: "PT Sans", sans-serif; color: var(--text); }

  .slide {
    position: absolute; width: 586px; height: 438px; overflow: hidden;
    background: linear-gradient(180deg, var(--pink-hi), var(--pink));
  }
  .slide--1 { left: 10px; top: 8px; background: linear-gradient(180deg, #fff, #f7eeee); }
  .slide--2 { left: 604px; top: 8px; }
  .slide--3 { left: 10px; top: 454px; }
  .slide--4 { left: 604px; top: 454px; }

  /* title slide */
  .hero-band {
    position: absolute; left: 0; top: 0; width: 100%; height: 262px;
    background: linear-gradient(180deg, var(--red-hi), var(--red) 60%, #8f141b);
    border-bottom: 6px solid var(--tan);
  }
  .hero-title {
    position: absolute; right: 34px; top: 96px;
    font: 700 33px/1 "PT Sans Narrow", sans-serif; color: var(--white);
  }
  .hero-sub {
    position: absolute; right: 34px; top: 140px; width: 340px; text-align: right;
    font: 400 13.5px/20px "PT Sans Narrow", sans-serif; color: var(--white);
  }
  .portrait-ring {
    position: absolute; left: 20px; top: 152px; width: 212px; height: 212px; border-radius: 50%;
    background: #f4dcd2; border: 4px solid #c7704f; padding: 8px;
  }
  .portrait {
    width: 100%; height: 100%; border-radius: 50%;
    background: radial-gradient(circle at 50% 40%, #d9cdc4, #a3928a 60%, #3a3438);
  }

  /* brand name */
  .brand { position: absolute; display: flex; align-items: center; gap: 10px; color: var(--maroon); font-family: "PT Sans", sans-serif; font-weight: 400; }
  .brand-dot { width: 16px; height: 16px; border-radius: 50%; background: var(--maroon); }
  .brand-text { display: flex; flex-direction: column; line-height: 1; }
  .brand-text .line1 { font-size: 23px; letter-spacing: 2px; }
  .brand-text .line2 { font-size: 13px; letter-spacing: 7px; margin-top: 4px; }
  .slide--1 .brand { left: 318px; top: 308px; }
  .slide .brand--corner { right: 12px; top: 352px; gap: 8px; }
  .brand--corner .brand-dot { width: 13px; height: 13px; }
  .brand--corner .line1 { font-size: 19px; }
  .brand--corner .line2 { font-size: 11px; letter-spacing: 5.6px; margin-top: 3px; }

  /* footer bar */
  .footer {
    position: absolute; left: 0; bottom: 0; width: 100%; height: 44px;
    background: linear-gradient(180deg, #b3212a, var(--red-deep));
    border-top: 3px solid var(--tan);
    display: flex; align-items: center; color: var(--white);
  }
  .slide-no {
    margin-left: 16px; width: 30px; height: 26px; display: grid; place-items: center;
    background: var(--orange); border: 1px solid #e9966a;
    font: 400 15px/1 "PT Sans", sans-serif;
  }
  .footer-note { margin-left: 20px; font: italic 400 14px/1 "PT Sans", sans-serif; }
  .slide--1 .footer-note { margin-left: 46px; font-weight: 700; }
  .nav { margin-left: auto; margin-right: 16px; display: flex; gap: 8px; }
  .btn {
    height: 26px; padding: 0 12px; display: grid; place-items: center;
    background: linear-gradient(180deg, var(--orange-hi), var(--orange));
    font: 400 12px/1 "PT Sans", sans-serif; color: var(--white); border-radius: 3px;
  }
  .btn--back { padding-left: 18px; clip-path: polygon(10px 0, 100% 0, 100% 100%, 10px 100%, 0 50%); border-radius: 0 3px 3px 0; }
  .btn--next { padding-right: 18px; clip-path: polygon(0 0, calc(100% - 10px) 0, 100% 50%, calc(100% - 10px) 100%, 0 100%); border-radius: 3px 0 0 3px; }

  /* content slides */
  .ribbon {
    position: absolute; left: 0; top: 12px; width: 22px; height: 30px;
    background: linear-gradient(180deg, var(--red-hi), var(--red-deep));
    clip-path: polygon(0 0, 100% 0, 100% 100%, 0 72%);
  }
  .slide-title {
    position: absolute; left: 28px; top: 13px;
    font: 700 26px/1 "PT Sans Narrow", sans-serif; color: var(--maroon);
  }
  .section-head {
    position: absolute; left: 44px; top: 72px;
    font: 700 16.5px/1 "PT Sans Narrow", sans-serif; color: var(--maroon);
  }
  .checklist {
    position: absolute; left: 46px; top: 100px; list-style: none;
    font: 400 12.5px/19px "PT Sans Narrow", sans-serif; color: var(--text);
  }
  .slide--3 .checklist { width: 480px; }
  .checklist li { position: relative; padding-left: 20px; }
  .checklist li::before {
    content: ""; position: absolute; left: 0; top: 4px; width: 11px; height: 11px;
    border: 1.5px solid var(--maroon); background: var(--white);
  }
  .checklist li::after {
    content: ""; position: absolute; left: 4px; top: 2px; width: 5px; height: 9px;
    border-right: 2.5px solid var(--maroon); border-bottom: 2.5px solid var(--maroon);
    transform: rotate(40deg);
  }
  .team-photo {
    position: absolute; left: 206px; top: 94px; width: 352px; height: 274px;
    background: linear-gradient(180deg, rgba(246,224,224,0) 0%, #5b4e4c 12%, #3b3a42 50%, #8a7f7c 72%, rgba(246,224,224,0) 100%);
  }
</style>
</head>
<body>

  <section class="slide slide--1">
    <div class="hero-band"></div>
    <h1 class="hero-title">Project Title Here</h1>
    <p class="hero-sub">Discover the edge. Optimize the whole.<br>Endpoint visibility, access and security</p>
    <div class="portrait-ring"><div class="portrait" role="img" aria-label="Portrait photo of the presenter"></div></div>
    <div class="brand"><span class="brand-dot"></span><span class="brand-text"><span class="line1">TALLOW CREST</span><span class="line2">SOFTWARE</span></span></div>
    <footer class="footer"><span class="slide-no">01</span><span class="footer-note">01/02/15</span><div class="nav"><span class="btn">Start</span></div></footer>
  </section>

  <section class="slide slide--2">
    <div class="ribbon"></div>
    <h2 class="slide-title">Thank You</h2>
    <div class="brand brand--corner"><span class="brand-dot"></span><span class="brand-text"><span class="line1">TALLOW CREST</span><span class="line2">SOFTWARE</span></span></div>
    <footer class="footer"><span class="slide-no">02</span><span class="footer-note">Discover the edge. Optimize the whole.</span><div class="nav"><span class="btn btn--back">Back</span><span class="btn btn--next">Next</span></div></footer>
  </section>

  <section class="slide slide--3">
    <div class="ribbon"></div>
    <h2 class="slide-title">Slide Title Presentation</h2>
    <h3 class="section-head">Something About Your Business</h3>
    <ul class="checklist">
      <li>Endpoint visibility built for enterprise IT teams</li>
      <li>Full insight into every device that touches the corporate network</li>
      <li>Real-time detection of suspicious activity across all endpoints</li>
      <li>“See Everything, Control Everything” approach to security</li>
      <li>Policy-based access control that blocks risky devices before they connect</li>
      <li>Trusted by Meridane 2,000 organizations around the world</li>
      <li>Clear, fast and actionable security reporting</li>
      <li>A platform that constantly tracks the latest threats, tools and standards to help IT departments stop data breaches early, all while fitting the systems and workflows they already rely on</li>
      <li>Scales from a single campus to global networks</li>
      <li>Not Just Visibility! We deliver control over the<br>whole network, through and through.</li>
    </ul>
    <div class="brand brand--corner"><span class="brand-dot"></span><span class="brand-text"><span class="line1">TALLOW CREST</span><span class="line2">SOFTWARE</span></span></div>
    <footer class="footer"><span class="slide-no">03</span><span class="footer-note">Discover the edge. Optimize the whole.</span><div class="nav"><span class="btn btn--back">Back</span><span class="btn btn--next">Next</span></div></footer>
  </section>

  <section class="slide slide--4">
    <div class="ribbon"></div>
    <h2 class="slide-title">Slide Title Presentation</h2>
    <h3 class="section-head">Our Services</h3>
    <ul class="checklist">
      <li>Device Discovery</li>
      <li>Asset Inventory</li>
      <li>Profiling</li>
      <li>Access Control</li>
      <li>Threat Alerts</li>
      <li>Guest Access</li>
      <li>Policy Enforcement</li>
      <li>Compliance</li>
      <li>Network Segmentation</li>
      <li>Reporting</li>
      <li>Integrations</li>
      <li>Support</li>
    </ul>
    <div class="team-photo" role="img" aria-label="Group photo of a business team standing together"></div>
    <div class="brand brand--corner"><span class="brand-dot"></span><span class="brand-text"><span class="line1">TALLOW CREST</span><span class="line2">SOFTWARE</span></span></div>
    <footer class="footer"><span class="slide-no">04</span><span class="footer-note">Discover the edge. Optimize the whole.</span><div class="nav"><span class="btn btn--back">Back</span><span class="btn btn--next">Next</span></div></footer>
  </section>

</body>
</html>
```